Kitchen and cabinet shop needs new website

Benvoe Cabinets is a mid-sized, family run cabinet shop that is in the process of updating it's image after being handed over to the second generation. It's been in the business for almost 30 years and our designers have lots of experience in the design, home building and renovation industry. Our business offers free home consultations or a customer can visit our showroom to start the design process. Whether the client is a designer, home builder or homeowner we can help create the kitchen and space you're after by helping every step of the way.

The website needs to showcase our past work, (pictures to be included), show the different styles (eg. traditional, modern) and different areas of the home we can produce cabinets for. We created a new logo with Sketch hive that needs to be included in the website as well as the colours. I would like 5 pages;
-Home page
-About us
-portfolio/gallery
-services
-contact us

I would like the website to have a contemporary look, nothing too busy or complicated.

I will attach some pictures with the different styles of our work I mentioned above and provide content for each job.
Updates

Target Market(s)

home owners, designer, home builders, business owners

Industry/Entity Type

Home Builder

Number of Pages Required

5+ page

Font styles to use
Sans Serif

Requirements
Must have
• home page, about us page, gallery/portfolio page-showing various pictures of our work and different styles, services page and contact us.
• Use logo and similar colours as in logo for the scheme
• more content and pictures to follow...

```html
<!DOCTYPE html>
<html lang="en">
<head>
<meta charset="utf-8">
<title>Benvoe Cabinets</title>
<link href="https://fonts.googleapis.com/css2?family=Open+Sans:wght@400;600;700&family=Raleway:wght@400;600;700&display=swap" rel="stylesheet">
<style>
:root{
  --blue:#1455a6;
  --orange:#f26f21;
  --ink:#333;
  --muted:#666;
  --light:#f7f7f7;
  --footer:#575757;
  --footer-text:#d9d9d9;
  --grey-sq:#8c8c8c;
}
*{margin:0;padding:0;box-sizing:border-box}
html,body{width:1037px;height:1200px;overflow:hidden;background:#fff;font-family:"Open Sans",sans-serif;color:var(--ink)}
.page{position:relative;width:1037px;height:1200px}
.abs{position:absolute}
.brand{left:86px;top:24px;display:flex;align-items:center;gap:8px}
.brand-mark{width:38px;height:50px;background:var(--orange)}
.brand-name{font-family:"Raleway",sans-serif;font-weight:700;font-size:24px;line-height:1;color:var(--blue);letter-spacing:1px}
.call{left:308px;top:32px;display:flex;align-items:center;gap:8px}
.call-label{font-family:"Raleway",sans-serif;font-size:13px;letter-spacing:2.5px;color:var(--ink);line-height:1}
.call-num{font-family:"Open Sans",sans-serif;font-weight:600;font-size:20px;color:var(--blue);line-height:1.1}
.social-top{left:869px;top:7px;display:flex;gap:8px}
.sq{width:22px;height:22px;display:block;background:var(--grey-sq)}
.sq.blue{background:var(--blue)}
.nav{top:59px;left:550px;display:flex;align-items:center;font-size:9px;text-transform:uppercase}
.nav a{color:var(--ink);text-decoration:none;line-height:29px}
.nav .active{background:var(--blue);color:#fff;font-weight:700;padding:0 11px;width:52px}
.hero{left:10px;top:96px;width:1016px;height:370px;background:linear-gradient(180deg,#e8e4df 0%,#e2dcd4 45%,#d9b58a 75%,#e9dccb 100%)}
.hero-arrow{top:244px;width:74px;height:74px;display:flex;align-items:center;justify-content:center}
.hero-arrow.prev{left:11px;background:#2f2f2f}
.hero-arrow.next{left:952px;background:var(--blue)}
.dots{left:492px;top:437px;display:flex;gap:4px}
.dot{width:14px;height:14px;background:#999}
.dot.on{background:var(--blue)}
.welcome{left:222px;top:500px;width:592px;text-align:center;font-family:"Raleway",sans-serif;font-weight:400;font-size:18px;padding-bottom:4px;border-bottom:1px solid #bbb;white-space:nowrap}
.welcome .b{color:var(--blue);font-weight:700;font-size:25px}
.welcome .o{color:var(--orange);font-weight:600;font-size:25px}
.lead{left:0;width:1037px;top:545px;text-align:center;font-family:"Raleway",sans-serif;font-size:14px}
.intro{left:230px;width:577px;top:569px;text-align:center;font-size:10.5px;line-height:15.5px;color:var(--muted)}
.btn{left:470px;top:611px;width:96px;height:29px;background:var(--blue);color:#fff;font-size:9.5px;font-weight:700;display:flex;align-items:center;justify-content:center}
.projects{left:0;top:680px;width:1037px;height:298px;background:var(--light)}
.projects h2{position:absolute;left:85px;top:34px;font-family:"Raleway",sans-serif;font-weight:700;font-size:18px;color:var(--orange)}
.tile{top:70px;width:422px;height:184px;display:flex;flex-direction:column;align-items:center;justify-content:center;gap:4px}
.tile.trad{left:85px;background:linear-gradient(180deg,#dca06a,#c9834a 60%,#b0703a)}
.tile.mod{left:530px;background:linear-gradient(180deg,#eeeeee,#dcdcdc 55%,#8a8b8e)}
.tile .ic{width:30px;height:30px;border-radius:50%;display:flex;align-items:center;justify-content:center}
.tile .label{font-family:"Raleway",sans-serif;font-size:13px;font-weight:600}
.footer{left:0;top:978px;width:1037px;height:222px;background:var(--footer);color:var(--footer-text)}
.footer h3{font-family:"Raleway",sans-serif;font-weight:600;font-size:18px;color:#d0d0d0;position:absolute;top:50px}
.f-brand{left:86px;top:84px;display:flex;align-items:center;gap:8px}
.f-brand .brand-mark{background:#cfcfcf}
.f-brand .brand-name{color:#cfcfcf}
.f-list{position:absolute;top:72px;font-size:11px;line-height:15px;list-style:none}
.f-contact{position:absolute;left:529px;top:72px;font-size:11px;font-weight:600;line-height:20px}
.f-contact div{display:flex;align-items:center;gap:8px}
.f-social{position:absolute;left:751px;top:80px;display:flex;gap:8px}
.copy{position:absolute;left:0;top:184px;width:1037px;border-top:1px solid #777;text-align:center;font-size:9px;padding-top:8px}
</style>
</head>
<body>
<div class="page">
  <header>
    <div class="abs brand"><span class="brand-mark"></span><span class="brand-name">BENVOE<br>CABINETS</span></div>
    <div class="abs call">
      <svg width="24" height="24" viewBox="0 0 24 24"><path fill="#1455a6" d="M6.6 10.8c1.4 2.8 3.8 5.1 6.6 6.6l2.2-2.2c.3-.3.7-.4 1-.2 1.1.4 2.3.6 3.6.6.6 0 1 .4 1 1V20c0 .6-.4 1-1 1C10.6 21 3 13.4 3 4c0-.6.4-1 1-1h3.5c.6 0 1 .4 1 1 0 1.3.2 2.5.6 3.6.1.3 0 .7-.2 1z"/></svg>
      <div><div class="call-label">CALL US NOW</div><div class="call-num">555-010-2020</div></div>
    </div>
    <div class="abs social-top"><span class="sq blue"></span><span class="sq"></span><span class="sq"></span></div>
    <nav class="abs nav">
      <a class="active" style="text-align:center">Home</a>
      <a style="margin-left:33px">About us</a>
      <a style="margin-left:48px">Gallery</a>
      <a style="margin-left:48px">Services</a>
      <a style="margin-left:46px">Contact us</a>
    </nav>
  </header>

  <div class="abs hero" role="img" aria-label="Photo of a modern kitchen with white cabinets, red backsplash and curved wooden bar counter"></div>
  <div class="abs hero-arrow prev"><svg width="12" height="14" viewBox="0 0 12 14"><path d="M8 1 2 7l6 6" stroke="#fff" stroke-width="2" fill="none"/></svg></div>
  <div class="abs hero-arrow next"><svg width="12" height="14" viewBox="0 0 12 14"><path d="m4 1 6 6-6 6" stroke="#fff" stroke-width="2" fill="none"/></svg></div>
  <div class="abs dots"><span class="dot"></span><span class="dot on"></span><span class="dot"></span></div>

  <h1 class="abs welcome">Welcome&nbsp; to <span class="b">BENVOE</span> <span class="o">CABINETS</span> Custom Woodwork and Cabinetry</h1>
  <p class="abs lead">Lorem Ipsum is simply dummy text of the printing and typesetting industry</p>
  <p class="abs intro">Lorem Ipsum is simply dummy text of the printing and typesetting industry. Lorem Ipsum has been the industry's standard dummy text ever since the 1500s, when an unknown printer took.</p>
  <a class="abs btn">Read More</a>

  <section class="abs projects">
    <h2>Latest Projects</h2>
    <div class="abs tile trad" role="img" aria-label="Photo of a traditional kitchen with warm wood tones">
      <span class="ic" style="background:#fff"><svg width="14" height="14" viewBox="0 0 14 14"><path d="M6 8 8 6M5 6 3 8a2 2 0 0 0 3 3l2-2M9 8l2-2a2 2 0 0 0-3-3L6 5" stroke="#f26f21" stroke-width="1.6" fill="none"/></svg></span>
      <span class="label" style="color:#fff">TRADITIONAL</span>
    </div>
    <div class="abs tile mod" role="img" aria-label="Photo of a modern white kitchen with island and bar stools">
      <span class="ic" style="background:#f26f21"><svg width="14" height="14" viewBox="0 0 14 14"><path d="M6 8 8 6M5 6 3 8a2 2 0 0 0 3 3l2-2M9 8l2-2a2 2 0 0 0-3-3L6 5" stroke="#fff" stroke-width="1.6" fill="none"/></svg></span>
      <span class="label" style="color:#f26f21">MODERN</span>
    </div>
  </section>

  <footer class="abs footer">
    <div class="abs f-brand"><span class="brand-mark"></span><span class="brand-name">BENVOE<br>CABINETS</span></div>
    <h3 style="left:307px">Navigaton</h3>
    <ul class="f-list" style="left:309px"><li>Home</li><li>About us</li><li>Gallery</li><li>Services</li><li>Contact us</li></ul>
    <h3 style="left:529px">Contact Us</h3>
    <div class="f-contact">
      <div><svg width="10" height="10" viewBox="0 0 24 24"><path fill="#eee" d="M6.6 10.8c1.4 2.8 3.8 5.1 6.6 6.6l2.2-2.2c.3-.3.7-.4 1-.2 1.1.4 2.3.6 3.6.6.6 0 1 .4 1 1V20c0 .6-.4 1-1 1C10.6 21 3 13.4 3 4c0-.6.4-1 1-1h3.5c.6 0 1 .4 1 1 0 1.3.2 2.5.6 3.6.1.3 0 .7-.2 1z"/></svg>555-010-2020</div>
      <div><svg width="11" height="9" viewBox="0 0 11 9"><rect width="11" height="9" fill="#eee"/><path d="m0 0 5.5 5L11 0" stroke="#575757" fill="none"/></svg>info@benvoecabinets.com</div>
      <div><svg width="10" height="11" viewBox="0 0 10 14"><path fill="#eee" d="M5 0a5 5 0 0 0-5 5c0 4 5 9 5 9s5-5 5-9a5 5 0 0 0-5-5zm0 7a2 2 0 1 1 0-4 2 2 0 0 1 0 4z"/></svg>your address benvoecabinets</div>
    </div>
    <h3 style="left:751px">Follow us on :</h3>
    <div class="f-social"><span class="sq blue"></span><span class="sq" style="background:#aaa"></span><span class="sq" style="background:#aaa"></span></div>
    <div class="copy">© 2015 copyrights BENVOE CABINETS. All Reserved</div>
  </footer>
</div>
</body>
</html>
```